High-end dermatology office brochure design

Corvellan Skin and Laser is a high-end dermatology practice that specializes in custom skin care solutions, and skin cancer surveillance and treatment. Brochure should be elegant, but informative to attract high-end customers.

Target Market(s)

Men and women 27-60

Industry/Entity Type

Office

Requirements
Must have
• Attached document has required copy, including, websites, address and company phone number
Nice to have
• images

```html
<!DOCTYPE html>
<html lang="en">
<head>
<meta charset="utf-8">
<title>Corvellan Skin and Laser – Brochure</title>
<link href="https://fonts.googleapis.com/css2?family=Pinyon+Script&family=Roboto+Condensed:wght@300;400;700&family=Open+Sans:wght@400;600&display=swap" rel="stylesheet">
<style>
  :root {
    --purple: #6a2f86;
    --purple-deep: #5b2674;
    --purple-bar: #4f1f66;
    --lilac: #b896c9;
    --lime: #cfe07a;
    --lime-pale: #eef4cc;
    --ink: #4a4a4a;
    --ink-soft: #6b6b6b;
    --skin: #f1ddd2;
    --stage: #262626;
    --script: "Pinyon Script", cursive;
    --cond: "Roboto Condensed", sans-serif;
    --body: "Open Sans", sans-serif;
  }
  * { margin: 0; padding: 0; box-sizing: border-box; }
  html, body { width: 1200px; height: 1200px; overflow: hidden; }
  body { background: var(--stage); position: relative; font-family: var(--body); }

  .sheet { position: absolute; left: 214px; width: 771px; height: 560px; overflow: hidden; background: #fff; }
  .sheet--front { top: 26px; }
  .sheet--inner { top: 614px; background: linear-gradient(180deg, #fff 40%, var(--lime-pale) 80%, #e2ec9c 100%); }
  .abs { position: absolute; }
  svg.layer { position: absolute; left: 0; top: 0; }

  /* front */
  .locations-panel { left: 0; top: 0; width: 386px; height: 300px; background: linear-gradient(180deg, #eef4cf 0%, #fff 60%); }
  .hero-photo { left: 386px; top: 0; width: 385px; height: 450px; background: linear-gradient(160deg, #e9cbbd 0%, var(--skin) 45%, #fbf3ef 100%); }
  .script-title { font-family: var(--script); color: var(--purple); font-size: 23px; white-space: nowrap; font-weight: 400; }
  .locations-title { left: 0; width: 386px; top: 40px; text-align: center; transform: translateY(-50%); }
  .location { position: absolute; top: 64px; width: 120px; margin-left: -60px; text-align: center; color: var(--ink); font-size: 6.6px; line-height: 9.2px; }
  .location__city { margin-bottom: 6px; }
  .location__map { display: block; margin: 0 auto 6px; }
  .tagline { left: 386px; width: 385px; top: 16px; text-align: center; font-family: var(--cond); line-height: 20px; }
  .tagline__lead { font-weight: 300; font-size: 16px; color: #6b4c7a; }
  .tagline__strong { font-weight: 700; font-size: 16px; color: var(--purple); }
  .brand { left: 470px; top: 338px; display: flex; align-items: center; gap: 6px; font-family: var(--cond); font-weight: 400; font-size: 20px; color: var(--purple); white-space: nowrap; }
  .brand__dot { width: 12px; height: 12px; border-radius: 50%; background: var(--lime); }
  .hours { left: 59px; top: 307px; color: #fff; font-family: var(--cond); font-weight: 300; font-size: 11px; line-height: 14px; white-space: nowrap; }
  .world-map { left: 26px; top: 362px; width: 176px; height: 88px; background: #7a3c96; border-radius: 40px 30px 50px 20px; opacity: .8; }
  .contact { left: 20px; top: 470px; color: #fff; font-family: var(--cond); }
  .contact__phone { font-size: 35px; font-weight: 300; line-height: 38px; padding-bottom: 2px; border-bottom: 1px dotted rgba(255,255,255,.8); }
  .contact__web { font-size: 10.5px; letter-spacing: 2px; line-height: 17px; border-bottom: 1px dotted rgba(255,255,255,.8); }
  .contact__shop { font-size: 10.5px; letter-spacing: 1.4px; line-height: 17px; }
  .promise { left: 386px; width: 385px; top: 460px; text-align: center; color: #fff; font-family: var(--cond); font-weight: 300; font-size: 16px; line-height: 20px; }
  .url-bar { left: 386px; top: 524px; width: 385px; height: 16px; background: var(--purple-bar); color: #eee; font-size: 7.5px; line-height: 16px; text-align: center; }

  /* inner */
  .face-photo { left: 480px; top: 30px; width: 291px; height: 260px; background: radial-gradient(ellipse at 55% 35%, rgba(241,221,210,.8) 0%, rgba(241,221,210,.45) 45%, rgba(255,255,255,0) 75%); }
  .product-photo { left: 184px; top: 150px; width: 200px; height: 118px; background: radial-gradient(ellipse at 60% 50%, #f3dcc6 0%, #f6eee6 40%, rgba(255,255,255,0) 75%); }
  .what-we-do { left: 60px; width: 276px; top: 32px; text-align: center; color: #fff; }
  .what-we-do .script-title { color: #fff; display: block; margin-bottom: 4px; }
  .what-we-do p { font-size: 7.4px; line-height: 16.4px; }
  .medical { left: 18px; top: 232px; width: 350px; color: var(--ink); font-size: 7.3px; line-height: 10.4px; }
  .medical .script-title { display: block; line-height: 26px; }
  .conditions { margin: 8px 0 0 48px; width: 242px; display: grid; grid-template-columns: 1fr 1fr; }
  .conditions li { list-style: none; font-family: var(--body); font-size: 15px; color: #7b6a86; line-height: 27px; border-bottom: 1px dotted #bdbdbd; display: flex; align-items: center; gap: 6px; }
  .conditions li:nth-last-child(-n+2) { border-bottom: none; }
  .medical p { margin-top: 10px; }
  .highlight { display: inline-block; background: var(--purple); color: #fff; padding: 1px 4px; font-weight: 600; }
  .services { left: 405px; top: 80px; width: 345px; color: var(--ink); font-size: 7.3px; line-height: 14.6px; }
  .services .script-title { display: block; line-height: 26px; }
  .services ul { list-style: none; color: var(--purple); font-weight: 600; }
  .services ul li::before { content: "• "; }
  .services .note { color: var(--purple); font-weight: 600; padding-left: 6px; }
  .services .gap-s { margin-top: 8px; }
  .services .gap-m { margin-top: 14px; }
  .services .gap-l { margin-top: 18px; }
  .services .label { font-weight: 600; color: #444; }
</style>
</head>
<body>

<section class="sheet sheet--front" aria-label="Brochure front">
  <div class="abs locations-panel"></div>
  <div class="abs hero-photo" role="img" aria-label="Close-up portrait photograph of a woman with clear skin"></div>

  <svg class="layer" width="771" height="560" viewBox="0 0 771 560">
    <path d="M0,244 C120,250 250,300 400,352 C520,394 600,410 660,400 C710,390 750,355 771,335 L771,560 L0,560 Z" fill="var(--lilac)"/>
    <path d="M0,243 C120,252 250,312 400,364 C520,410 600,430 660,420 C710,410 750,380 771,362 L771,560 L0,560 Z" fill="var(--lime)"/>
    <path d="M0,250 C120,258 250,320 400,372 C520,420 600,442 660,434 C710,426 750,400 771,388 L771,560 L0,560 Z" fill="var(--purple)"/>
  </svg>

  <h2 class="abs script-title locations-title">Visit Our Location</h2>

  <div class="location" style="left:84px">
    <div class="location__city">Phoenix, Arizona</div>
    <svg class="location__map" width="88" height="88" viewBox="0 0 88 88" role="img" aria-label="Street map of the Phoenix office">
      <circle cx="44" cy="44" r="42" fill="#dedcd8" stroke="var(--lime)" stroke-width="3"/>
      <path d="M44,30 a6,6 0 0 1 6,6 c0,5 -6,11 -6,11 s-6,-6 -6,-11 a6,6 0 0 1 6,-6z" fill="#d9443a"/>
    </svg>
    <div>Corvellan Skin &amp; Laser<br>2710 E Mesa Verde Rd<br>Building # 4<br>Suite # 112<br>Phoenix, AZ 85048</div>
  </div>
  <div class="location" style="left:198px">
    <div class="location__city">Scottsdale, Arizona</div>
    <svg class="location__map" width="88" height="88" viewBox="0 0 88 88" role="img" aria-label="Street map of the Scottsdale office">
      <circle cx="44" cy="44" r="42" fill="#dedcd8" stroke="var(--lime)" stroke-width="3"/>
      <path d="M52,14 a6,6 0 0 1 6,6 c0,5 -6,11 -6,11 s-6,-6 -6,-11 a6,6 0 0 1 6,-6z" fill="#d9443a"/>
    </svg>
    <div>Verdant Skin Studio<br>Located in Wellpoint Suites<br>7420 E Saguaro Ln<br>Suite # 206<br>Scottsdale, AZ 85258</div>
  </div>
  <div class="location" style="left:310px">
    <div class="location__city">Honolulu, Hawaii</div>
    <svg class="location__map" width="88" height="88" viewBox="0 0 88 88" role="img" aria-label="Street map of the Honolulu office">
      <circle cx="44" cy="44" r="42" fill="#dedcd8" stroke="var(--lime)" stroke-width="3"/>
      <path d="M44,30 a6,6 0 0 1 6,6 c0,5 -6,11 -6,11 s-6,-6 -6,-11 a6,6 0 0 1 6,-6z" fill="#d9443a"/>
    </svg>
    <div>Pacific Skin Cancer Clinic<br>Harbor View Plaza<br>Suite # 310<br>820 Kaimana Blvd<br>Honolulu, HI 96815</div>
  </div>

  <div class="abs tagline">
    <div class="tagline__lead">A personalized approach to skin care.</div>
    <div class="tagline__strong">Results you can see. Care you can feel</div>
  </div>

  <div class="abs brand"><span>Corvellan Skin and Laser</span><span class="brand__dot"></span></div>

  <svg class="abs" style="left:22px;top:307px" width="28" height="28" viewBox="0 0 28 28" aria-hidden="true">
    <circle cx="14" cy="14" r="12.5" fill="none" stroke="#fff" stroke-width="1.5"/>
    <path d="M14,7 V14 L19,16" fill="none" stroke="#fff" stroke-width="1.5" stroke-linecap="round"/>
  </svg>
  <div class="abs hours">Monday - Thursday 8:00am - 5:30pm<br>Friday 8:00am - 2:30pm but can vary</div>

  <div class="abs world-map" role="img" aria-label="World map showing office locations"></div>

  <div class="abs contact">
    <div class="contact__phone">480-555-0172</div>
    <div class="contact__web">www.corvellanskincare.com</div>
    <div class="contact__shop">Shop at: www.shopcorvellan.com</div>
  </div>

  <p class="abs promise">Let us create a custom skin care regimen that best<br>fits your medical and personal needs</p>
  <div class="abs url-bar">www.corvellanskincare.com</div>
</section>

<section class="sheet sheet--inner" aria-label="Brochure inside">
  <div class="abs face-photo" role="img" aria-label="Soft portrait photograph of a smiling woman touching her cheek"></div>
  <svg class="layer" width="771" height="560" viewBox="0 0 771 560">
    <defs>
      <linearGradient id="innerPurple" x1="0" y1="0" x2="0" y2="1">
        <stop offset="0" stop-color="#8a4ea3"/>
        <stop offset="1" stop-color="#9a66b0"/>
      </linearGradient>
    </defs>
    <path d="M0,0 H771 V78 C700,30 560,20 480,40 C420,58 380,90 320,120 C230,165 110,168 0,140 Z" fill="url(#innerPurple)"/>
  </svg>
  <div class="abs product-photo" role="img" aria-label="Photograph of a cream jar with white jasmine flowers"></div>

  <div class="abs what-we-do">
    <h2 class="script-title">What We Do</h2>
    <p>We pride ourselves on providing premium skin care, to patients of all ages, with an honest and attentive approach. We're also proud to be leaders in skin cancer surveillance and specialize in the diagnosis and treatment of skin cancer.</p>
  </div>

  <div class="abs medical">
    <h2 class="script-title">Medical Services</h2>
    <div>We're leaders in the diagnosis of all skin conditions and autoimmune skin conditions, including:</div>
    <ul class="conditions">
      <li><svg width="14" height="12" viewBox="0 0 14 12" aria-hidden="true"><path d="M1,6 L5,10 L13,1" fill="none" stroke="#6aa83a" stroke-width="2.4"/></svg>Rashes</li>
      <li><svg width="14" height="12" viewBox="0 0 14 12" aria-hidden="true"><path d="M1,6 L5,10 L13,1" fill="none" stroke="#6aa83a" stroke-width="2.4"/></svg>Skin tags</li>
      <li><svg width="14" height="12" viewBox="0 0 14 12" aria-hidden="true"><path d="M1,6 L5,10 L13,1" fill="none" stroke="#6aa83a" stroke-width="2.4"/></svg>Acne</li>
      <li><svg width="14" height="12" viewBox="0 0 14 12" aria-hidden="true"><path d="M1,6 L5,10 L13,1" fill="none" stroke="#6aa83a" stroke-width="2.4"/></svg>Rosacea</li>
      <li><svg width="14" height="12" viewBox="0 0 14 12" aria-hidden="true"><path d="M1,6 L5,10 L13,1" fill="none" stroke="#6aa83a" stroke-width="2.4"/></svg>Warts</li>
      <li><svg width="14" height="12" viewBox="0 0 14 12" aria-hidden="true"><path d="M1,6 L5,10 L13,1" fill="none" stroke="#6aa83a" stroke-width="2.4"/></svg>Psoriasis</li>
    </ul>
    <p style="margin-top:24px">We're also involved in ongoing research for the treatment of psoriasis</p>
    <p>Skin cancer surveillance and treatment<br>Skin cancer can form anywhere on the skin (even where the sun doesn't shine), so it's vital that a full body exam is done at least once a year.</p>
    <p><span class="highlight">We pride ourselves on thorough surveillance and commitment to your overall health.</span></p>
    <p>Alternative care<br>Your commitment to your health is the same as our commitment to you. We provide non-antibiotic acne treatment including botanicals, blue light and a combination of supplements to fit your personal lifestyle.</p>
  </div>

  <div class="abs services">
    <h2 class="script-title">Dermatologic Surgery Services</h2>
    <div>We have in-house surgeons for the removal of atypical moles and skin cancers, including margin control for melanoma. Our board-certified, in-house surgeons specialize in:</div>
    <ul>
      <li>Plastic surgery</li>
      <li>Mohs surgery</li>
    </ul>
    <div class="note">(treatment includes transportation and care from your trusted healthcare team)</div>
    <h2 class="script-title gap-s">Cosmetic services</h2>
    <div>Your skin is unique, so we take pride in our ability to provide personalized consultations and skin care analysis to set you up with the right treatments and products.</div>
    <ul class="gap-m">
      <li>Chemical peels</li>
      <li>Photofacial</li>
      <li>Ultrasound lift</li>
      <li>Laser resurfacing</li>
      <li>IPL</li>
      <li>Injectables and fillers (Velari, Luvessa, Sorelle, Neurella and Dermalyn)</li>
    </ul>
    <div class="gap-l"><span class="label">Elite-grade cosmeceutical products</span><br>Including Corlane, Jana Moreau, Lumivra, Solenne Mineral, Dermivane, Lashora and much more.</div>
    <div class="gap-m"><span class="label">Esthetic services</span><br>Facials, peels, microdermabrasion, body wraps, waxing, eyelash extensions, brow tinting</div>
    <h2 class="script-title gap-m">Nutrition and Supplement Support</h2>
    <div>Including gluten free, no filler multi-vitamins, immune boosters, hormone, sleep aid balancing products and B12 injections and the Lean Shot.</div>
  </div>
</section>

</body>
</html>
```